Psychiatrist/ Psychotherapist needs a letterhead design

I am a Psychiatrist working in private practice. I work as a psychotherapist and treat patients with depression, anxiety, post traumatic stress and relationship problems. I need a letterhead which is elegant and professional. I would like to see designs using colours such as blues and greys.
I would like the information on the letterhead split between the top and bottom of the page to give it a look of balance.
I want it to look elegant, feminine and upmarket. I don't want it to look too corporate but to show some flair and to be a bit artistic.

Target Market(s)

Other doctors, specialists and agencies who have referred patients to me.

Industry/Entity Type

Work

Font styles to use
Script

Requirements
Must have
• My name and my profession psychiatrist need to be highlighted and prominent. It needs to be professional looking and elegant without being old fashioned or too conservative.
Nice to have
• Balance between the top and bottom of the page.
Should not have
• I don't want fonts which are old and too traditional.

```html
<!DOCTYPE html>
<html lang="en">
<head>
<meta charset="utf-8">
<title>Dr. Clara Whitmore – Stationery</title>
<link href="https://fonts.googleapis.com/css2?family=Cinzel:wght@600&family=Source+Sans+3:wght@400;600;700&display=swap" rel="stylesheet">
<style>
  :root {
    --page-bg: #f1f1f1;
    --paper: #ffffff;
    --navy: #1f3f7d;
    --navy-dark: #1c2f68;
    --navy-light: #2560a8;
    --accent: #1f78c1;
    --ink: #3a3a3a;
    --grey: #5a5a5a;
  }
  * { box-sizing: border-box; margin: 0; padding: 0; }
  html, body { width: 1200px; height: 1000px; overflow: hidden; }
  body {
    background: var(--page-bg);
    font-family: "Source Sans 3", Arial, sans-serif;
    position: relative;
  }

  .card {
    position: absolute;
    left: 60px;
    width: 370px;
    height: 215px;
    background: var(--paper);
    overflow: hidden;
  }
  .card--front-dark { top: 70px; background: linear-gradient(180deg, var(--navy-light), var(--navy-dark)); }
  .card--front-light { top: 325px; border-top: 9px solid var(--accent); border-bottom: 9px solid var(--accent); }
  .card--back { top: 580px; border-bottom: 9px solid var(--accent); }

  .wordmark {
    position: absolute;
    left: 0; right: 0;
    text-align: center;
  }
  .wordmark__name {
    font-family: "Cinzel", Georgia, serif;
    font-weight: 600;
    font-size: 24px;
    color: var(--navy);
    letter-spacing: 0.5px;
    white-space: nowrap;
  }
  .wordmark__title {
    font-size: 12px;
    letter-spacing: 7px;
    color: var(--navy);
    margin-top: 6px;
    padding-left: 7px;
  }
  .card--front-dark .wordmark { top: 80px; }
  .card--front-dark .wordmark__name,
  .card--front-dark .wordmark__title { color: #ffffff; }
  .card--front-light .wordmark { top: 72px; }

  .card__holder { position: absolute; left: 38px; top: 16px; }
  .card__holder-name { font-weight: 700; font-size: 18px; color: var(--accent); line-height: 1.1; }
  .card__holder-role { font-size: 12px; color: var(--grey); }

  .contact {
    position: absolute;
    text-align: right;
    color: var(--ink);
  }
  .contact__row { white-space: nowrap; }
  .contact__label { font-weight: 700; color: var(--accent); }
  .contact__gap { height: 6px; }
  .card--back .contact { right: 26px; top: 96px; font-size: 10.5px; line-height: 15px; }

  .letterhead {
    position: absolute;
    left: 460px;
    top: 45px;
    width: 660px;
    height: 910px;
    background: var(--paper);
    border-bottom: 10px solid var(--accent);
  }
  .letterhead .wordmark {
    left: 45px; right: auto; top: 38px;
    text-align: left;
  }
  .letterhead .wordmark__name { font-size: 27px; }
  .letterhead .wordmark__title { padding-left: 48px; font-size: 12px; }
  .letterhead .contact {
    right: 38px; bottom: 26px;
    font-size: 13px; line-height: 19px;
  }
</style>
</head>
<body>

  <section class="card card--front-dark" aria-label="Business card front, navy">
    <div class="wordmark">
      <div class="wordmark__name">Dr. Clara Whitmore</div>
      <div class="wordmark__title">PSYCHIATRIST</div>
    </div>
  </section>

  <section class="card card--front-light" aria-label="Business card front, white">
    <div class="wordmark">
      <div class="wordmark__name">Dr. Clara Whitmore</div>
      <div class="wordmark__title">PSYCHIATRIST</div>
    </div>
  </section>

  <section class="card card--back" aria-label="Business card back">
    <div class="card__holder">
      <div class="card__holder-name">Clara Whitmore</div>
      <div class="card__holder-role">Psychiatrist</div>
    </div>
    <div class="contact">
      <div class="contact__row"><span class="contact__label">Tel:</span> (08) 8215 4407</div>
      <div class="contact__row"><span class="contact__label">Fax:</span> (08) 8215 4490</div>
      <div class="contact__row"><span class="contact__label">Mob:</span> 0412557093</div>
      <div class="contact__gap"></div>
      <div class="contact__row">cwhitmore@mailhub.net.au</div>
      <div class="contact__row">14 Miller Lane, Norwood, SA 5067</div>
    </div>
  </section>

  <section class="letterhead" aria-label="Letterhead">
    <div class="wordmark">
      <div class="wordmark__name">Dr. Clara Whitmore</div>
      <div class="wordmark__title">PSYCHIATRIST</div>
    </div>
    <div class="contact">
      <div class="contact__row"><span class="contact__label">Tel:</span> (08) 8215 4407</div>
      <div class="contact__row"><span class="contact__label">Fax:</span> (08) 8215 4490</div>
      <div class="contact__row"><span class="contact__label">Mob:</span> 0412557093</div>
      <div class="contact__gap"></div>
      <div class="contact__row">cwhitmore@mailhub.net.au</div>
      <div class="contact__row">14 Miller Lane, Norwood, SA 5067</div>
    </div>
  </section>

</body>
</html>
```